Ferncrest Dental, LLC business card project

Business card to be designed with current logo.
Dental office- please keep design of card that looks clean and professional.
Please include the following info:
Ferncrest Dental, LLC
Dr. Lorna Pettigrew
2871 Marlowe Street
Halden Ridge, OR 97485
541-555-0193
ferncrestdental.office@examplemail.test
Hello everyone-
Reason: Just got back from overseas- will look at all designs and provide feedback. Thank you!
Reason: Polling my friends for the final selection-
thank you to all those that participated- so many talented designers!

```html
<!DOCTYPE html>
<html lang="en">
<head>
<meta charset="utf-8">
<title>Ferncrest Dental, LLC – Business Card</title>
<link rel="stylesheet" href="https://fonts.googleapis.com/css2?family=Comfortaa:wght@400&family=Didact+Gothic&family=Cabin:wght@600&display=swap">
<style>
  :root {
    --card-white: #ffffff;
    --leaf-green: #65a045;
    --deep-green: #5f9a3c;
    --lime: #a9c93a;
    --text-light: #ffffff;
  }
  html, body {
    margin: 0;
    padding: 0;
    overflow: hidden;
    background: var(--card-white);
  }
  .card {
    position: relative;
    width: 1200px;
    height: 686px;
    background: var(--card-white);
    overflow: hidden;
  }
  .brand {
    position: absolute;
    left: 24px;
    top: 62px;
    display: flex;
    align-items: center;
    gap: 18px;
  }
  .brand-dot {
    width: 58px;
    height: 58px;
    border-radius: 50%;
    background: var(--lime);
  }
  .brand-name {
    font-family: "Comfortaa", sans-serif;
    font-weight: 400;
    font-size: 54px;
    color: var(--leaf-green);
    letter-spacing: -1px;
    line-height: 1;
  }
  .practitioner {
    position: absolute;
    left: 760px;
    top: 38px;
  }
  .doctor-name {
    margin: 0;
    font-family: "Didact Gothic", sans-serif;
    font-weight: 400;
    font-size: 46px;
    color: var(--deep-green);
    line-height: 1.2;
    white-space: nowrap;
  }
  .company-name {
    margin: 8px 0 0;
    font-family: "Cabin", sans-serif;
    font-weight: 600;
    font-size: 41px;
    color: var(--lime);
    letter-spacing: 0.5px;
    line-height: 1.2;
    white-space: nowrap;
  }
  .contact-band {
    position: absolute;
    left: 0;
    top: 379px;
    width: 1200px;
    height: 307px;
    background: var(--leaf-green);
  }
  .contact-list {
    list-style: none;
    margin: 0;
    padding: 16px 0 0 32px;
    font-family: "Didact Gothic", sans-serif;
    font-size: 50px;
    color: var(--text-light);
    line-height: 67px;
    white-space: nowrap;
  }
</style>
</head>
<body>
  <main class="card">
    <div class="brand">
      <span class="brand-dot"></span>
      <span class="brand-name">Ferncrest Dental</span>
    </div>

    <div class="practitioner">
      <h1 class="doctor-name">Dr. Lorna Pettigrew</h1>
      <p class="company-name">Ferncrest Dental, LLC</p>
    </div>

    <section class="contact-band">
      <ul class="contact-list">
        <li class="street">2871 Marlowe Street</li>
        <li class="city">Halden Ridge, OR 97485</li>
        <li class="phone">541-555-0193</li>
        <li class="email">ferncrestdental.office@examplemail.test</li>
      </ul>
    </section>
  </main>
</body>
</html>
```